Eco-friendly waste company needs flyer design to promote collections

We need a flyer to promote our new small item collection service, offering cheaper waste collections to customers who usually would not want to pay for our high-eco performance business (we are expensive compared to companies who dispose of their waste in less eco-friendly ways). This flyer needs to be professional, informational, and classy to appeal to corporate office-based customers. We want photos used where possible, not cartoon or illustrations of objects we collect. I will attach our logo in various designs, and am really open to design options. We have a website that is ourdated, uses cartoons etc, and this is not landing well with our customer base so we want to move away from that kind of design. I need an A5-sized flyer, double sided. Please ask me if you have any questions!
Hi all,
Thank you all so much for so many wonderful designs, I will be looking through all of these tomorrow with my CEO and then I will update the project status again.
Thanks!!
Kind regards,
Lena

Hi all,
Thanks!!
Kind regards,
Lena

```html
<!DOCTYPE html>
<html lang="en">
<head>
<meta charset="utf-8">
<title>Brightbin – Collection Flyers</title>
<link href="https://fonts.googleapis.com/css2?family=Montserrat:wght@400;500;600;700;800;900&display=swap" rel="stylesheet">
<style>
:root{
  --teal:#2fae86;
  --teal-bright:#4fd0a4;
  --teal-pale:#7ff0cc;
  --ink:#2b2b28;
  --charcoal:#3a3a36;
  --footer:#454545;
  --panel:#ebebeb;
  --white:#ffffff;
}
*{margin:0;padding:0;box-sizing:border-box}
html,body{width:1200px;height:1200px;overflow:hidden;background:var(--white);font-family:"Montserrat",sans-serif;color:var(--ink)}
.canvas{position:relative;width:1200px;height:1200px}
.flyer{position:absolute;top:261px;width:529px;height:686px;background:var(--white);box-shadow:0 3px 10px rgba(0,0,0,.25);overflow:hidden}
.flyer--front{left:55px}
.flyer--back{left:625px}
.flyer__bg{position:absolute;inset:0;width:529px;height:686px}
.abs{position:absolute}
.brand{display:flex;align-items:center;gap:8px}
.brand__square{flex:none}
.brand__name{font-weight:700;letter-spacing:.5px;line-height:1}
.tagline{font-weight:700;text-transform:uppercase;letter-spacing:.2px}

/* front */
.front-brand{left:21px;top:34px}
.front-brand .brand__square{width:14px;height:14px;background:var(--teal)}
.front-brand .brand__name{font-size:20px;color:var(--ink)}
.front-tagline{left:21px;top:62px;font-size:5.5px;color:var(--teal)}
.headline{left:20px;top:86px;font-weight:900;text-transform:uppercase;line-height:1}
.headline__big{font-size:30px;color:var(--ink);display:block}
.headline__mid{font-size:17.5px;color:var(--ink);display:block;margin-top:4px}
.headline__teal{font-size:18px;color:var(--teal);display:block;margin-top:3px;line-height:1.1}
.headline-rule{left:20px;top:181px;width:222px;height:1.5px;background:var(--ink)}
.intro{left:19px;top:191px;width:200px;font-size:7.2px;line-height:1.3;font-weight:500}
.items-title{left:21px;top:280px;font-size:14px;font-weight:600;color:var(--white);letter-spacing:.3px}
.item{position:absolute;display:flex;align-items:center;gap:11px;color:var(--white);font-size:8.2px;font-weight:700;line-height:1.25}
.item svg{width:20px;height:20px;flex:none}
.item small{display:block;font-size:6px;font-weight:500}
.challenge{left:37px;top:489px;width:456px;height:61px;background:var(--charcoal);border-radius:12px;color:var(--white);font-size:19.5px;font-weight:600;text-align:center;line-height:1.15;padding-top:8px}
.conditions{left:19px;top:564px;width:491px;height:39px;border:1.5px solid #8b8b8b;border-radius:20px;overflow:hidden;display:flex}
.conditions__label{width:137px;background:var(--teal);color:var(--white);font-size:12px;font-weight:600;display:flex;align-items:center;padding-left:7px;position:relative}
.conditions__label::after{content:"";position:absolute;right:-5px;top:15px;border-left:5px solid var(--teal);border-top:5px solid transparent;border-bottom:5px solid transparent}
.conditions__text{padding:4px 0 0 9px;font-size:7.3px;font-weight:500;line-height:2.05}
.footer-bar{left:0;top:627px;width:529px;height:32px;background:var(--footer)}
.footer-ask{font-size:7px;font-weight:700;color:var(--teal-bright);line-height:1.45}
.footer-mail{display:flex;align-items:center;gap:5px;font-size:6.4px;color:var(--white)}
.footer-mail svg{width:11px;height:11px}
.call-tab{top:621px;height:45px;background:linear-gradient(90deg,var(--teal),var(--teal-bright));color:var(--white)}
.call-tab__lead{font-size:10px;font-weight:800;letter-spacing:.3px}
.call-tab__phone{font-size:20px;font-weight:800;display:flex;align-items:center;gap:10px;letter-spacing:.5px}
.call-tab__phone svg{width:18px;height:18px}

/* back */
.back-brand{left:21px;top:34px}
.back-brand .brand__square{width:18px;height:18px;background:var(--white)}
.back-brand .brand__name{font-size:26px;color:var(--white)}
.back-tagline{left:21px;top:72px;font-size:7px;color:var(--white);font-weight:600}
.back-headline{left:21px;top:122px;font-size:24.5px;font-weight:900;color:var(--white);line-height:1.01;text-transform:uppercase}
.back-rule{left:21px;top:228px;width:175px;height:1.5px;background:var(--white)}
.collect-title{left:20px;top:317px;font-size:16px;line-height:1.15}
.collect-title b{color:var(--teal);font-weight:800;display:block}
.collect-title span{font-weight:500;color:var(--ink)}
.collect-rule{left:21px;top:357px;width:265px;height:1.5px;background:var(--teal)}
.check{position:absolute;left:20px;display:flex;gap:13px;font-size:8px;font-weight:700;line-height:1.3}
.check svg{width:13px;height:13px;flex:none;margin-top:-1px}
.check em{font-style:normal;color:var(--teal)}
.shred-box{left:21px;top:563px;width:265px;height:41px;background:var(--teal);border-radius:7px;color:var(--white);font-size:8px;font-weight:800;padding:9px 0 0 9px;line-height:1.2;text-transform:uppercase}
.data-panel{left:300px;top:288px;width:208px;height:316px;background:var(--panel);border-bottom-left-radius:26px}
.data-title{left:314px;top:321px;font-size:9.5px;font-weight:800;line-height:1.05;text-transform:uppercase}
.data-title b{color:var(--teal);display:block;font-weight:800}
.data-copy{position:absolute;left:314px;width:190px;font-size:6.6px;line-height:1.3;color:#555}
.data-include{left:314px;top:403px;font-size:8.3px;font-weight:700}
.data-item{position:absolute;display:flex;align-items:center;gap:6px;font-size:8px;font-weight:500;line-height:1.1}
.data-item i{width:8px;height:7px;border:1.3px solid var(--teal);border-radius:1px;flex:none}
</style>
</head>
<body>
<main class="canvas">

  <!-- FRONT -->
  <section class="flyer flyer--front">
    <svg class="flyer__bg" viewBox="0 0 529 686" aria-hidden="true">
      <defs>
        <linearGradient id="tealFill" x1="0" y1="0" x2="1" y2="0">
          <stop offset="0" stop-color="#2fa883"/>
          <stop offset=".5" stop-color="#4ccca2"/>
          <stop offset="1" stop-color="#2fa883"/>
        </linearGradient>
        <linearGradient id="photoTone" x1="0" y1="0" x2="1" y2="1">
          <stop offset="0" stop-color="#b9a98e"/>
          <stop offset=".5" stop-color="#8c8f99"/>
          <stop offset="1" stop-color="#6d6154"/>
        </linearGradient>
      </defs>
      <path d="M0 226 H529 V486 Q300 530 0 514 Z" fill="url(#tealFill)"/>
      <rect x="280" y="0" width="249" height="270" fill="url(#photoTone)" role="img" aria-label="Photo of a recycling worker in hard hat, mask and orange overalls in a sorting hall"/>
      <path d="M180 255 Q360 310 529 248 V268 Q360 320 180 270 Z" fill="#7ff0cc"/>
      <circle cx="110" cy="58" r="204" fill="#2fae86"/>
      <circle cx="110" cy="58" r="198" fill="#ffffff"/>
    </svg>

    <div class="abs brand front-brand"><span class="brand__square"></span><span class="brand__name">BRIGHTBIN</span></div>
    <div class="abs tagline front-tagline">Responsible disposal, every time</div>

    <h1 class="abs headline">
      <span class="headline__big">Do you have</span>
      <span class="headline__mid">Small or single items</span>
      <span class="headline__teal">That cost too much<br>to dispose of?</span>
    </h1>
    <div class="abs headline-rule"></div>
    <p class="abs intro">Are you located in Central London? Brightbin has the solution for you. We can collect items for £25 each on Wednesdays.</p>

    <h2 class="abs items-title">OUR EXAMPLE ITEMS ARE:</h2>

    <div class="item" style="left:20px;top:319px"><svg viewBox="0 0 20 20" fill="none" stroke="#fff" stroke-width="1.6"><rect x="2" y="9" width="16" height="8" rx="1"/><path d="M5 9V2h8l2 2v5"/></svg>Printers</div>
    <div class="item" style="left:181px;top:319px"><svg viewBox="0 0 20 20" fill="none" stroke="#fff" stroke-width="1.6"><rect x="1" y="4" width="13" height="10" rx="1"/><rect x="15" y="2" width="4" height="14"/><path d="M5 17h5"/></svg>PC or Television<br>Monitors</div>
    <div class="item" style="left:350px;top:319px"><svg viewBox="0 0 20 20" fill="none" stroke="#fff" stroke-width="1.6"><rect x="4" y="2" width="12" height="11"/><path d="M1 15h18M1 18h18M10 6v5M8 8l2-2 2 2"/></svg>Pallet</div>

    <div class="item" style="left:20px;top:360px"><svg viewBox="0 0 20 20" fill="none" stroke="#fff" stroke-width="1.6"><path d="M1 7h18v3H1zM3 10v8M17 10v8M8 13h5M10 13v5"/></svg>Office Furniture</div>
    <div class="item" style="left:181px;top:360px"><svg viewBox="0 0 20 20" fill="none" stroke="#fff" stroke-width="1.6"><circle cx="10" cy="8" r="7"/><circle cx="10" cy="8" r="2"/><path d="M10 15v3M6 19h8"/></svg>Fans</div>
    <div class="item" style="left:350px;top:356px"><svg viewBox="0 0 20 20" fill="none" stroke="#fff" stroke-width="1.6"><path d="M2 6l8-4 8 4v9l-8 4-8-4z M2 6l8 4 8-4M10 10v9"/></svg><span>Packaging<small>(cardboard boxes, polystyrene,<br>plastic etc.)</small></span></div>

    <div class="item" style="left:20px;top:406px"><svg viewBox="0 0 20 20" fill="none" stroke="#fff" stroke-width="1.6"><rect x="2" y="2" width="16" height="13"/><path d="M1 15h18M3 15l-1 4M17 15l1 4"/></svg>Whiteboards</div>
    <div class="item" style="left:181px;top:404px"><svg viewBox="0 0 20 20" fill="none" stroke="#fff" stroke-width="1.6"><path d="M4 11h12l-2 8H6zM10 11V5M10 5c-3 0-4-2-4-4 3 0 4 2 4 4zM10 6c2 0 4-1 4-4"/></svg>Plants and Planter<br>Boxes</div>
    <div class="item" style="left:350px;top:404px"><svg viewBox="0 0 20 20" fill="none" stroke="#fff" stroke-width="1.6"><path d="M18 2l-8 8M9 9l2 2-5 7-5-5z"/></svg><span>Paints and chemicals<small>(max 7 litres)</small></span></div>

    <div class="item" style="left:20px;top:450px"><svg viewBox="0 0 20 20" fill="none" stroke="#fff" stroke-width="1.6"><rect x="2" y="6" width="16" height="6" rx="1"/><path d="M5 6V2h10v4M5 12v6M8 12v6M11 12v6M14 12v6"/></svg>Shredders</div>
    <div class="item" style="left:181px;top:446px"><svg viewBox="0 0 20 20" fill="none" stroke="#fff" stroke-width="1.6"><path d="M10 4v14M10 4C7 2 4 2 1 3v14c3-1 6-1 9 1 3-2 6-2 9-1V3c-3-1-6-1-9 1z"/></svg><span>Books and Magazines<small>(Max 25kgs)</small></span></div>
    <div class="item" style="left:350px;top:442px"><svg viewBox="0 0 20 20" fill="none" stroke="#fff" stroke-width="1.6"><path d="M7 14c0-3-2-4-2-7a5 5 0 0110 0c0 3-2 4-2 7zM8 17h4M10 0v1M1 7h1M18 7h1"/></svg><span>Light bulbs and<br>fluorescent tubes<small>(max 10 pieces)</small></span></div>

    <div class="abs challenge">We can take most things you can’t put<br>in your normal bins – challenge us!</div>

    <div class="abs conditions">
      <div class="conditions__label">Conditions of offer:</div>
      <div class="conditions__text">Price is exclusive of VAT.<br>Eligible postcodes: EC1, EC2, EC3, EC4, WC1, WC2, W1, SW1, SE1, E1, E2, N1, NW1</div>
    </div>

    <div class="abs footer-bar"></div>
    <div class="abs footer-ask" style="left:19px;top:632px">If You Have Any Questions<br>Please Email Us:</div>
    <div class="abs footer-mail" style="left:152px;top:637px"><svg viewBox="0 0 12 12" fill="none" stroke="#4fd0a4" stroke-width="1.2"><rect x="1" y="3" width="10" height="8"/><path d="M1 3l5 4 5-4"/></svg>bookings@brightbin.example</div>
    <div class="abs call-tab" style="left:317px;width:212px;border-radius:22px 0 0 22px;padding:4px 21px 0 0;text-align:right">
      <div class="call-tab__lead">OR CALL US NOW!</div>
      <div class="call-tab__phone" style="justify-content:flex-end"><svg viewBox="0 0 20 20" fill="none" stroke="#2b2b28" stroke-width="2"><path d="M5 2l3 4-2 2c1 3 3 5 6 6l2-2 4 3-2 3C9 18 2 11 2 4z"/></svg>020 4000 1234</div>
    </div>
  </section>

  <!-- BACK -->
  <section class="flyer flyer--back">
    <svg class="flyer__bg" viewBox="0 0 529 686" aria-hidden="true">
      <defs>
        <linearGradient id="leafTone" x1="0" y1="0" x2="1" y2="1">
          <stop offset="0" stop-color="#5f9a32"/>
          <stop offset=".55" stop-color="#34621f"/>
          <stop offset="1" stop-color="#1c2a15"/>
        </linearGradient>
      </defs>
      <path d="M0 0 H529 V276 Q420 300 300 284 Q150 262 0 306 Z" fill="url(#leafTone)" role="img" aria-label="Photo of cupped hands holding dark soil with a young green seedling"/>
      <path d="M0 306 Q150 262 300 284 Q420 300 529 276 V290 Q420 312 300 296 Q150 276 0 318 Z" fill="#2fae86"/>
    </svg>

    <div class="abs brand back-brand"><span class="brand__square"></span><span class="brand__name">BRIGHTBIN</span></div>
    <div class="abs tagline back-tagline">Responsible disposal, every time</div>
    <h1 class="abs back-headline">Need to get rid<br>of items which<br>can’t go in your<br>normal bin?</h1>
    <div class="abs back-rule"></div>

    <div class="abs data-panel"></div>

    <h2 class="abs collect-title"><b>WE COLLECT THE</b><span>FOLLOWING HAZARDOUS ITEMS:</span></h2>
    <div class="abs collect-rule"></div>

    <div class="check" style="top:372px"><svg viewBox="0 0 14 14" fill="none" stroke="#2fae86" stroke-width="1.4"><rect x="1" y="1" width="11" height="11"/><path d="M3 6l3 3 7-8"/></svg><span>Paint - <em>£4 per litre</em></span></div>
    <div class="check" style="top:391px"><svg viewBox="0 0 14 14" fill="none" stroke="#2fae86" stroke-width="1.4"><rect x="1" y="1" width="11" height="11"/><path d="M3 6l3 3 7-8"/></svg><span>Fluorescent tubes and bulbs - <em>£4 each</em></span></div>
    <div class="check" style="top:410px"><svg viewBox="0 0 14 14" fill="none" stroke="#2fae86" stroke-width="1.4"><rect x="1" y="1" width="11" height="11"/><path d="M3 6l3 3 7-8"/></svg><span>Cooking oil / hydraulic oil / hazardous liquids –<br><em>from £5 per litre</em></span></div>
    <div class="check" style="top:440px"><svg viewBox="0 0 14 14" fill="none" stroke="#2fae86" stroke-width="1.4"><rect x="1" y="1" width="11" height="11"/><path d="M3 6l3 3 7-8"/></svg><span>TV / Computer monitors - <em>£10 each</em></span></div>
    <div class="check" style="top:464px"><svg viewBox="0 0 14 14" fill="none" stroke="#2fae86" stroke-width="1.4"><rect x="1" y="1" width="11" height="11"/><path d="M3 6l3 3 7-8"/></svg><span>Batteries – <em>from £5 per kilo (depends on type)</em></span></div>
    <div class="check" style="top:487px"><svg viewBox="0 0 14 14" fill="none" stroke="#2fae86" stroke-width="1.4"><rect x="1" y="1" width="11" height="11"/><path d="M3 6l3 3 7-8"/></svg><span>Gas bottles &amp; fire extinguishers - £35 each<br>Fridges – <em>£40 for a small fridge, £125 for a<br>commercial fridge, £200 for an ammonia<br>fridge each</em></span></div>
    <div class="check" style="top:539px"><svg viewBox="0 0 14 14" fill="none" stroke="#2fae86" stroke-width="1.4"><rect x="1" y="1" width="11" height="11"/><path d="M3 6l3 3 7-8"/></svg><span>Air conditioners - <em>£30 each</em></span></div>

    <div class="abs shred-box">We can also securely destroy any paper, files<br>documents etc with our shredding service.</div>

    <h2 class="abs data-title"><b>Need to securely destroy</b>Data on your computer or<br>server?</h2>
    <p class="data-copy" style="top:362px">We can securely collect and wipe your data-holding electrical items, allowing for their safe reuse. Items that fail the wiping process will be securely shredded and recycled.</p>
    <div class="abs data-include">Items include:</div>

    <div class="data-item" style="left:314px;top:424px"><i></i>Computers</div>
    <div class="data-item" style="left:314px;top:443px"><i></i>Laptops</div>
    <div class="data-item" style="left:314px;top:462px"><i></i>Servers</div>
    <div class="data-item" style="left:314px;top:480px"><i></i>Routers</div>
    <div class="data-item" style="left:314px;top:499px"><i></i>Switches</div>
    <div class="data-item" style="left:381px;top:424px"><i></i>Mobile phones</div>
    <div class="data-item" style="left:381px;top:443px"><i></i>Landline phones</div>
    <div class="data-item" style="left:381px;top:462px"><i></i>Printers with memory</div>
    <div class="data-item" style="left:381px;top:480px"><i></i>Photocopiers with<br>memory</div>

    <p class="data-copy" style="top:526px;font-size:7.2px">We can provide certificates confirming data secure destruction, either through securing wiping and reuse, or through shredding and recycling.</p>
    <p class="data-copy" style="top:567px;font-size:7.2px">We can also securely destroy any paper, files, documents etc with our shredding service.</p>

    <div class="abs footer-bar"></div>
    <div class="abs call-tab" style="left:0;width:231px;border-radius:0 22px 22px 0;padding:4px 0 0 21px">
      <div class="call-tab__lead">CALL US NOW!</div>
      <div class="call-tab__phone"><svg viewBox="0 0 20 20" fill="none" stroke="#2b2b28" stroke-width="2"><path d="M5 2l3 4-2 2c1 3 3 5 6 6l2-2 4 3-2 3C9 18 2 11 2 4z"/></svg>020 4000 1234</div>
    </div>
    <div class="abs footer-ask" style="left:241px;top:632px">If You Have Any Questions<br>Please Email Us:</div>
    <div class="abs footer-mail" style="left:365px;top:637px"><svg viewBox="0 0 12 12" fill="none" stroke="#4fd0a4" stroke-width="1.2"><rect x="1" y="3" width="10" height="8"/><path d="M1 3l5 4 5-4"/></svg>bookings@brightbin.example</div>
  </section>

</main>
</body>
</html>
```